Business card design for upmarket Home Technology design and Installation company

Hello designers, we need a great business card designed.
We need it to convey high tech, and also sophistication .
We work with some of the most affluent people in the world building them home technology systems, and A/V entertainment systems.

Services offered include the following:
Design, sales, installation, and maintenance of

*Home Automation systems
*Distributed / Multi-Room Audio and Video
*High Performance Networks & WiFi
* Lighting and Shade Control
*Home cinema
*Security and CCTV Systems

I have included a copy of our logo to use for your design efforts.

Target Market(s)

Upmarket clients with multi million euro villas.

Industry/Entity Type

Home technology

Contact Information for Business Card

NAME: Derek Halloran ADDRESS: Plaza Brisa Local 42, Port Serralta, 07392 PHONE: +34-602-518-794 EMAIL: DHalloran@VELTRAsmarthomes.com WEB: www.veltrasmarthomes.com

Requirements
Must have
• Our Logo, and our tagline

```html
<!DOCTYPE html>
<html lang="en">
<head>
<meta charset="utf-8">
<title>VELTRA Smart Homes – Business Card</title>
<link rel="stylesheet" href="https://fonts.googleapis.com/css2?family=Dosis:wght@400;500&family=Nunito+Sans:wght@400&display=swap">
<style>
  :root {
    --backdrop: #d1d1d1;
    --card-light: #ffffff;
    --card-dark: #1f1f1d;
    --gold: #c9a457;
    --ink: #111111;
    --ink-soft: #6a6a6a;
    --ink-muted: #7d7d7d;
  }
  * { margin: 0; padding: 0; box-sizing: border-box; }
  html, body {
    width: 1200px;
    height: 1000px;
    overflow: hidden;
    background: var(--backdrop);
  }
  .canvas {
    position: relative;
    width: 1200px;
    height: 1000px;
  }
  .card {
    position: absolute;
    left: 305px;
    width: 613px;
    height: 352px;
    border-radius: 28px;
  }
  .card--front { top: 86px; background: var(--card-light); }
  .card--back  { top: 499px; background: var(--card-dark); }

  .front-info {
    position: absolute;
    right: 56px;
    top: 0;
    text-align: right;
  }
  .brand-name {
    font-family: "Dosis", sans-serif;
    font-weight: 500;
    color: var(--gold);
    line-height: 1;
    white-space: nowrap;
  }
  .front-info .brand-name {
    position: absolute;
    right: -10px;
    top: 56px;
    font-size: 38px;
    letter-spacing: 10px;
  }
  .address {
    position: absolute;
    right: -2px;
    top: 106px;
    font-family: "Nunito Sans", sans-serif;
    font-size: 12.5px;
    letter-spacing: 2.2px;
    line-height: 18px;
    color: var(--ink-soft);
    text-transform: uppercase;
    white-space: nowrap;
  }
  .person-name {
    position: absolute;
    right: -1px;
    top: 168px;
    font-family: "Dosis", sans-serif;
    font-weight: 400;
    font-size: 33px;
    line-height: 1.1;
    letter-spacing: 1.5px;
    color: var(--ink);
    text-transform: uppercase;
    white-space: nowrap;
  }
  .phone {
    position: absolute;
    right: -3px;
    top: 225px;
    font-family: "Dosis", sans-serif;
    font-size: 22px;
    letter-spacing: 3px;
    color: var(--ink);
    white-space: nowrap;
  }
  .email {
    position: absolute;
    right: -2px;
    top: 256px;
    font-family: "Nunito Sans", sans-serif;
    font-size: 12.5px;
    letter-spacing: 2px;
    color: var(--ink-muted);
    text-transform: uppercase;
    white-space: nowrap;
  }
  .website {
    position: absolute;
    right: -2px;
    top: 296px;
    font-family: "Nunito Sans", sans-serif;
    font-size: 10.5px;
    letter-spacing: 2px;
    color: var(--ink-soft);
    text-transform: uppercase;
    white-space: nowrap;
  }

  .back-brand {
    position: absolute;
    right: 46px;
    bottom: 42px;
    display: flex;
    align-items: center;
    gap: 12px;
  }
  .back-brand .brand-name { font-size: 30px; letter-spacing: 6px; margin-right: -6px; }
  .back-brand .brand-dot {
    width: 12px;
    height: 12px;
    border-radius: 50%;
    background: var(--gold);
  }
</style>
</head>
<body>
  <main class="canvas">
    <section class="card card--front" aria-label="Business card front">
      <div class="front-info">
        <div class="brand-name">VELTRA</div>
        <p class="address">Plaza Brisa Local 42<br>Port Serralta, 07392</p>
        <h1 class="person-name">Derek Halloran</h1>
        <p class="phone">+34-602-518-794</p>
        <p class="email">DHalloran@VELTRAsmarthomes.com</p>
        <p class="website">www.veltrasmarthomes.com</p>
      </div>
    </section>

    <section class="card card--back" aria-label="Business card back">
      <div class="back-brand">
        <span class="brand-dot"></span>
        <span class="brand-name">VELTRA</span>
      </div>
    </section>
  </main>
</body>
</html>
```